Wobble Tin Circle - New Website Design

Create a professional Shopify website for a the hottest trend; a slime subscription box business. Storvanta.com is an easy to use website builder.
Please see http://pellowhub.com and zinterpak.com for the concept I am after. The business has not been launched yet, I am currently in the pre-launch stage using a specialized landing page website, and so the time scale for developing my professional looking Shopify website is up to 1-2 weeks.
The webpage should have a fun feel and should match the style of the company logo at pellowhub.com. The pages to include are 'Home', 'About us' and 'Get Started'
Thank you and good luck!
Business
Coded - Design and coding required
1 page

```html
<!DOCTYPE html>
<html lang="en">
<head>
<meta charset="utf-8">
<title>Wobble Tin Circle</title>
<link href="https://fonts.googleapis.com/css2?family=Pacifico&family=Ubuntu:wght@400;500;700&display=swap" rel="stylesheet">
<style>
:root{
  --green:#138a1c;
  --green-dark:#0e6b14;
  --yellow:#f3e21b;
  --cream:#faf6ef;
  --ink:#1e1e1e;
  --muted:#666;
  --footer:#1b241e;
  --footer-text:#a9aea9;
  --white:#fff;
  --script:'Pacifico', cursive;
  --sans:'Ubuntu', sans-serif;
}
*{box-sizing:border-box;margin:0;padding:0}
html,body{width:1200px;height:2397px;overflow:hidden}
body{position:relative;font-family:var(--sans);color:var(--ink);background:var(--cream)}
.abs{position:absolute}

/* header */
.site-header{position:absolute;left:0;top:0;width:1200px;height:70px;background:var(--white);z-index:3}
.brand{position:absolute;left:210px;top:20px;display:flex;align-items:center;gap:8px}
.brand-dot{width:26px;height:26px;border-radius:50%;background:var(--green)}
.brand-name{font-family:var(--sans);font-weight:700;font-size:20px;color:var(--ink)}
.main-nav a{position:absolute;top:29px;font-size:12.5px;font-weight:500;color:var(--ink);text-decoration:none}
.account{position:absolute;left:989px;top:26px;width:20px;height:20px;border-radius:50%;background:var(--green)}

/* hero */
.hero{position:absolute;left:0;top:70px;width:1200px;height:405px;overflow:hidden}
.hero-photo{position:absolute;inset:0;background:linear-gradient(180deg,#b99a76 0%,#a98a6a 35%,#c9bfb3 60%,#3e9a2a 85%,#2f8c1d 100%)}
.hero-curve{position:absolute;left:0;bottom:0}
.hero-title{position:absolute;left:0;top:100px;width:1200px;text-align:center;font-family:var(--script);font-size:41px;line-height:50px;color:var(--white)}
.btn-yellow{position:absolute;left:528px;top:242px;width:145px;height:45px;border-radius:23px;background:var(--yellow);font-weight:700;font-size:14.5px;line-height:45px;text-align:center;color:var(--ink)}

/* sections */
.section-title{position:absolute;left:0;width:1200px;text-align:center;font-family:var(--script);font-size:37px;color:var(--green)}
.section-lead{position:absolute;left:280px;width:640px;text-align:center;font-size:11px;line-height:19px;color:var(--muted)}

.step{position:absolute;top:670px;width:250px;text-align:center}
.step-icon{width:75px;height:75px;margin:0 auto;border-radius:50%;background:#f6ebad;display:flex;align-items:center;justify-content:center}
.step h3{margin-top:20px;font-size:14.5px;font-weight:500}
.step p{margin-top:10px;font-size:10.5px;line-height:16px;color:var(--muted)}

/* plans */
.plans{position:absolute;left:0;top:915px;width:1200px;height:582px;background:linear-gradient(135deg,#3f8f3a 0%,#2e7f2c 40%,#4c9a46 70%,#37852f 100%)}
.plans .section-title{color:var(--white)}
.plans .section-lead{color:#e8f3e6}
.plan-card{position:absolute;background:var(--white);border:4px solid #2a2a2a;border-radius:16px;text-align:center}
.plan-card.featured{border-color:var(--yellow)}
.plan-card h3{font-size:25px;font-weight:500;margin-top:14px}
.plan-price{font-size:13px;color:var(--muted);margin-top:2px}
.plan-visual{margin:10px auto 0;width:210px;height:132px;border-radius:6px}
.btn-green{position:absolute;left:46px;width:173px;height:38px;border-radius:19px;background:var(--green);color:var(--white);font-size:12px;font-weight:700;line-height:38px}

/* inside */
.inside-box{position:absolute;left:393px;top:1675px;width:415px;height:340px;background:linear-gradient(180deg,#2f9a6a 0%,#8c6a45 30%,#a07a50 60%,#7b5a38 100%);border-radius:4px}
.callout{position:absolute;width:220px}
.callout h4{font-size:14px;font-weight:500}
.callout p{margin-top:6px;font-size:10.5px;line-height:16px;color:var(--muted)}
.callout.right-align{text-align:right}
.callout-line{position:absolute;height:1.5px;background:#e2cf1a}
.callout-dot{position:absolute;width:7px;height:7px;border-radius:50%;background:#e2cf1a}

/* footer */
.site-footer{position:absolute;left:0;top:2072px;width:1200px;height:325px;background:var(--footer)}
.footer-col{position:absolute;top:43px;width:200px}
.footer-col h5{font-size:14px;font-weight:500;color:#e9d41a}
.footer-col ul{list-style:none;margin-top:14px}
.footer-col li{font-size:11px;color:var(--footer-text);height:22.5px}
.footer-col li::before{content:"›";color:#e9d41a;margin-right:10px}
.footer-col p{margin-top:14px;font-size:11px;line-height:17px;color:var(--footer-text)}
.newsletter{position:absolute;left:0;top:129px;width:191px;height:24px;display:flex}
.newsletter-input{flex:1;background:var(--white);font-size:10px;font-style:italic;color:#555;padding:6px 8px}
.newsletter-send{width:24px;background:var(--green);display:flex;align-items:center;justify-content:center}
.cards{position:absolute;left:0;top:133px;display:flex;gap:3px}
.cards span{width:30px;height:20px;border-radius:2px}
.footer-rule{position:absolute;left:177px;top:205px;width:850px;height:1px;background:#3a443d}
.copyright{position:absolute;left:177px;top:219px;font-size:10.5px;color:var(--footer-text)}
.social{position:absolute;top:213px;width:28px;height:28px;border-radius:50%;border:1px solid #4b554e}
</style>
</head>
<body>

<header class="site-header">
  <div class="brand"><span class="brand-dot"></span><span class="brand-name">Wobble Tin Circle</span></div>
  <nav class="main-nav">
    <a style="left:735px">Home</a>
    <a style="left:802px">About Us</a>
    <a style="left:882px">Get Started</a>
  </nav>
  <span class="account" aria-label="Account"></span>
</header>

<section class="hero">
  <div class="hero-photo" role="img" aria-label="Photo of two children playing in a bathtub full of green slime"></div>
  <svg class="hero-curve" width="1200" height="40" viewBox="0 0 1200 40" aria-hidden="true">
    <path d="M0 40 L0 30 Q600 -10 1200 30 L1200 40 Z" fill="#faf6ef"/>
  </svg>
  <h1 class="hero-title">Happiness at your doorstep<br>every month</h1>
  <div class="btn-yellow">Get Started</div>
</section>

<section class="how">
  <h2 class="section-title" style="top:525px">How it works</h2>
  <p class="section-lead" style="top:602px">Lorem ipsum dolor sit amet, consectetur adipiscing elit, sed do eiusmod tempor incididunt ut labore et dolore magna aliqua. Ut enim ad minim veniam.</p>

  <div class="step" style="left:182px">
    <div class="step-icon">
      <svg width="30" height="36" viewBox="0 0 30 36" aria-hidden="true"><rect x="7" y="2" width="16" height="5" rx="1" fill="none" stroke="#111" stroke-width="2.5"/><rect x="4" y="7" width="22" height="27" rx="4" fill="none" stroke="#111" stroke-width="2.5"/><path d="M15 26 L9 20 a3.5 3.5 0 0 1 6-4 a3.5 3.5 0 0 1 6 4 Z" fill="#111"/></svg>
    </div>
    <h3>Pick your slimes</h3>
    <p>Lorem ipsum dolor sit amet, consectetuer adipiscing elit, sed diam nonummy nibh eui smod tincidunt ut laoreet dolore</p>
  </div>
  <div class="step" style="left:476px">
    <div class="step-icon">
      <svg width="38" height="36" viewBox="0 0 38 36" aria-hidden="true"><rect x="3" y="10" width="32" height="8" fill="#111"/><rect x="6" y="18" width="26" height="16" fill="#111"/><rect x="17" y="10" width="4" height="24" fill="#f6ebad"/><path d="M19 10 C12 2 6 6 12 10 M19 10 C26 2 32 6 26 10" stroke="#111" stroke-width="2.5" fill="none"/></svg>
    </div>
    <h3>Get at doorstep</h3>
    <p>Lorem ipsum dolor sit amet, consectetuer adipiscing elit, sed diam nonummy nibh eui smod tincidunt ut laoreet dolore</p>
  </div>
  <div class="step" style="left:767px">
    <div class="step-icon">
      <svg width="40" height="40" viewBox="0 0 40 40" aria-hidden="true"><circle cx="20" cy="20" r="8" fill="#111"/><g stroke="#111" stroke-width="5" stroke-linecap="round"><path d="M20 4 V12"/><path d="M20 28 V36"/><path d="M4 20 H12"/><path d="M28 20 H36"/><path d="M8 8 L14 14"/><path d="M26 26 L32 32"/><path d="M32 8 L26 14"/><path d="M8 32 L14 26"/></g></svg>
    </div>
    <h3>Enjoy happiness</h3>
    <p>Lorem ipsum dolor sit amet, consectetuer adipiscing elit, sed diam nonummy nibh eui smod tincidunt ut laoreet dolore</p>
  </div>
</section>

<section class="plans" role="region" aria-label="Choose a plan">
  <h2 class="section-title" style="top:50px">Choose a plan</h2>
  <p class="section-lead" style="top:120px">Lorem ipsum dolor sit amet, consectetur adipiscing elit, sed do eiusmod tempor incididunt ut labore et dolore magna aliqua. Ut enim ad minim veniam.</p>

  <div class="plan-card" style="left:175px;top:228px;width:265px;height:270px">
    <h3>Gold</h3>
    <div class="plan-price">Monthly / $5.99</div>
    <div class="plan-visual" role="img" aria-label="Product photo of a slime starter kit with colourful tubs" style="background:linear-gradient(90deg,#6fb64a,#e8c43a,#e06a8a)"></div>
    <div class="btn-green" style="top:216px">Get Started</div>
  </div>

  <div class="plan-card featured" style="left:467px;top:183px;width:267px;height:315px">
    <h3>Premium</h3>
    <div class="plan-price">6 months / $15.99</div>
    <div class="plan-visual" role="img" aria-label="Product photo of a display box of slime tubs" style="background:linear-gradient(180deg,#2f8a3a,#3d6a36 60%,#9aa19a)"></div>
    <div class="btn-green" style="top:261px">Get Started</div>
  </div>

  <div class="plan-card" style="left:759px;top:228px;width:265px;height:270px">
    <h3>Super</h3>
    <div class="plan-price">12 months / $39.99</div>
    <div class="plan-visual" role="img" aria-label="Product photo of a slime lab kit with bottles" style="background:linear-gradient(90deg,#2c4a9a,#d8a43a,#3aa04a)"></div>
    <div class="btn-green" style="top:210px">Get Started</div>
  </div>
</section>

<section class="inside">
  <h2 class="section-title" style="top:1535px">What's Inside?</h2>
  <p class="section-lead" style="top:1595px;left:390px;width:420px">Lorem ipsum dolor sit amet, consectetur adipiscing elit, sed do eiusmod tempor incididunt ut labore et dolore magna aliqua.</p>

  <div class="inside-box" role="img" aria-label="Photo of an open subscription box filled with slime tubs and treats"></div>

  <div class="callout right-align" style="left:140px;top:1795px"><h4>Slime Ice cream cone</h4><p>(Lipsum dolor sit amet, ullamcorper suscipit lobortis nisl ut aliquip)</p></div>
  <div class="callout-line" style="left:368px;top:1806px;width:100px"></div>
  <div class="callout-dot" style="left:465px;top:1803px"></div>

  <div class="callout right-align" style="left:140px;top:1941px"><h4>Fluffy Slime</h4><p>(El illum dolore eu feugiat nulla facilisis at vero eros et accumsan)</p></div>
  <div class="callout-line" style="left:368px;top:1950px;width:125px"></div>
  <div class="callout-dot" style="left:490px;top:1947px"></div>

  <div class="callout" style="left:841px;top:1843px"><h4>Slime pops</h4><p>(Nam liber tempor cum soluta nobis eleifend)</p></div>
  <div class="callout-line" style="left:718px;top:1853px;width:115px"></div>
  <div class="callout-dot" style="left:713px;top:1850px"></div>

  <div class="callout" style="left:841px;top:1928px"><h4>Sweet slime</h4><p>(Claritas est etiam processus dynamicus, qui sequitur nem)</p></div>
  <div class="callout-line" style="left:652px;top:1937px;width:181px"></div>
  <div class="callout-dot" style="left:647px;top:1934px"></div>
</section>

<footer class="site-footer">
  <div class="footer-col" style="left:177px">
    <h5>About Wobble Tin Circle</h5>
    <ul><li>About us</li><li>Our slimes</li><li>How it works</li><li>Blog</li></ul>
  </div>
  <div class="footer-col" style="left:398px">
    <h5>Support</h5>
    <ul><li>Contact us</li><li>Shipping rates &amp;</li><li>Delivery times</li><li>FAQs</li><li>Gift card</li></ul>
  </div>
  <div class="footer-col" style="left:617px">
    <h5>Newsletter</h5>
    <p>Subscribe to our newsletter and know about our latest offers and deals.</p>
    <div class="newsletter">
      <div class="newsletter-input">Enter email id...</div>
      <div class="newsletter-send"><svg width="12" height="12" viewBox="0 0 12 12" aria-hidden="true"><path d="M1 6 L11 1 L8 11 L6 7 Z" fill="#fff"/></svg></div>
    </div>
  </div>
  <div class="footer-col" style="left:838px">
    <h5>Payment option</h5>
    <p>Sed ut perspiciatis unde omnis iste natus error accusantium.</p>
    <div class="cards" aria-label="Accepted payment cards">
      <span style="background:#f2f2f2"></span><span style="background:#e8e8e8"></span><span style="background:#5b9bd5"></span><span style="background:#f0f0f0"></span>
    </div>
  </div>
  <div class="footer-rule"></div>
  <div class="copyright">Copyright © Wobble Tin Circle 2017</div>
  <span class="social" style="left:912px" aria-label="Social link"></span>
  <span class="social" style="left:952px" aria-label="Social link"></span>
  <span class="social" style="left:992px" aria-label="Social link"></span>
</footer>

</body>
</html>
```